Tradeo Cup Championship Webdesign project

We need a webdesign for the project called TradeoCup. TradeoCup™ is an international Forex trading competition to see who can make the most profit in two weeks with all players getting an equal starting sum. Participation is free with no strings attached and the prize money is real, with a total prize pool of $50,000! At the moment TradeoCup vol. 2 is about to get launched and we would like to have a new design. On the new website traders should be able to create their own competitions, as well as to invite each other for the cometition.
Updates

Project Deadline Extended

Project Deadline Extended

Requirements
Must have
• http://www.tradeocup-example.com/ please refer to this website for the further details.

The website should also include the competition section where traders can invite each other for the competition. It should work similarly to poker competitions.

```html
<!DOCTYPE html>
<html lang="en">
<head>
<meta charset="utf-8">
<title>TradeoCup – Trading Championship</title>
<link href="https://fonts.googleapis.com/css2?family=Arimo:wght@400;700&display=swap" rel="stylesheet">
<style>
:root{
  --page-top:#f4f4f4;
  --page-top-dark:#cfcfcf;
  --band-dark:#2b2b2b;
  --band-mid:#4a4a4a;
  --sky-light:#e4eef8;
  --sky-deep:#4f86c9;
  --white:#ffffff;
  --text:#333333;
  --text-soft:#555555;
  --brand-blue:#3f7cc4;
  --brand-blue-light:#8fb8e4;
  --tab-blue:#a9c9ea;
  --panel-bg:#f3f3f3;
  --panel-line:#dcdcdc;
  --prize-yellow:#ffd200;
  --prize-edge:#e0a800;
  --orange:#f06a12;
  --footer:#3a3a3a;
  --footer-text:#e8e8e8;
  --counter-bg:#2a2a2a;
}
*{box-sizing:border-box;margin:0;padding:0}
html,body{width:933px;height:1200px;overflow:hidden}
body{
  position:relative;
  font-family:"Arimo",Arial,sans-serif;
  color:var(--text);
  background:
    linear-gradient(var(--page-top),var(--page-top-dark)) 0 0/100% 105px no-repeat,
    linear-gradient(var(--band-mid),var(--band-dark) 40%,var(--band-mid)) 0 105px/100% 240px no-repeat,
    linear-gradient(var(--sky-light),#b9d3ee 45%,var(--sky-deep)) 0 345px/100% 855px no-repeat;
}
.abs{position:absolute}

/* header */
.logo-tab{left:150px;top:0;width:210px;height:98px;border-radius:0 0 10px 10px;
  background:linear-gradient(#b9d5f1,#5d92cf);display:flex;align-items:center;justify-content:center;gap:10px}
.logo-tab .mark{width:22px;height:22px;border-radius:50%;background:var(--white)}
.logo-tab .name{font-size:27px;color:var(--white);font-weight:400}
.account-links{left:640px;top:11px;display:flex;gap:8px}
.account-links a{display:block;width:64px;height:16px;border:1px solid #bbb;border-radius:8px;background:var(--white);
  font-size:10px;color:#333;text-align:center;line-height:14px;text-decoration:none}
.countdown-label{left:452px;top:22px;font-size:11px;color:#222}
.countdown{left:450px;top:35px;width:113px;height:35px;background:var(--counter-bg);padding:3px 4px}
.countdown .digits{display:flex;gap:3px}
.countdown .digits span{background:#555;color:var(--white);font-size:13px;font-weight:700;padding:1px 2px}
.countdown .digits small{font-size:8px}
.countdown .check{font-size:7px;color:var(--white);margin:4px 0 0 16px}
.lang{left:565px;top:35px;width:80px;height:35px;background:var(--counter-bg);padding:3px}
.lang .select{background:var(--white);height:13px;font-size:9px;padding-left:3px;line-height:13px;position:relative}
.lang .select::after{content:"";position:absolute;right:0;top:0;width:11px;height:13px;background:#ddd}
.lang .flag{width:13px;height:9px;background:#b03040;margin:5px auto 0}
.participants{left:655px;top:37px;width:118px;height:35px;display:flex}
.participants .label{width:65px;background:#777;color:var(--white);font-size:10px;font-weight:700;padding:4px 5px;line-height:11px}
.participants .count{flex:1;background:var(--brand-blue-light);color:var(--white);font-size:18px;font-weight:700;text-align:center;line-height:35px}
.main-nav{left:408px;top:85px;display:flex;gap:4px}
.main-nav a{display:block;height:20px;padding:0 9px;background:linear-gradient(var(--white),#ddd);border:1px solid #aaa;
  font-size:10px;color:#222;line-height:18px;text-decoration:none;border-radius:2px 2px 0 0}

/* page shell */
.shell{left:150px;top:105px;width:633px;height:1031px;background:var(--white);border-radius:6px 6px 10px 10px;overflow:hidden}
.hero{left:0;top:8px;width:438px;height:210px;background:linear-gradient(100deg,#1f5ea8,#5b95d3 45%,#9cc0e4 70%,#5f7f9e)}
.hero p{position:absolute;left:12px;top:16px;width:185px;font-size:9.5px;line-height:12px;color:var(--white)}
.hero .more{position:absolute;left:100px;top:104px;font-size:10px;color:var(--white);text-decoration:underline}
.hero .join{position:absolute;left:90px;top:135px;width:76px;height:22px;background:var(--orange);border-radius:4px;
  color:var(--white);font-size:11px;font-weight:700;text-align:center;line-height:22px}
.hero .dots{position:absolute;left:36px;top:188px;display:flex;gap:4px}
.hero .dots i{width:12px;height:12px;border-radius:50%;background:var(--white)}
.hero .dots i:first-child{background:var(--prize-yellow)}
.prize{left:447px;top:8px;width:183px;height:210px;background:var(--prize-yellow);border:2px solid var(--prize-edge);
  display:flex;align-items:center;justify-content:center;text-align:center;font-size:19px;line-height:23px;color:#222}

.panel{left:12px;background:var(--panel-bg);border:1px solid var(--panel-line)}
.tournaments{top:228px;width:423px;height:327px;background:var(--white)}
.tabs{position:absolute;left:4px;top:10px;display:flex;gap:4px}
.tabs span{width:134px;height:25px;font-size:11px;text-align:center;line-height:24px;border:1px solid #bbb;
  background:linear-gradient(#cfe2f5,var(--tab-blue));color:#234}
.tabs span.active{background:var(--white);border-bottom-color:var(--white);font-weight:700;color:#222}
.tab-body{position:absolute;left:14px;top:50px;width:395px;height:268px;overflow:hidden}
.tab-body p{font-size:7.8px;line-height:10px;color:#333;margin-bottom:6px}
.map-panel{top:570px;height:270px;width:423px}
.map{position:absolute;left:42px;top:17px;width:344px;height:234px;background:linear-gradient(#4d97d8,#cfe5f6 60%,#eaf4fb)}
.map span{position:absolute;left:6px;bottom:4px;font-size:14px;color:#555}
.banner-panel{top:852px;height:66px;width:423px}
.banner{position:absolute;left:55px;top:14px;width:313px;height:36px;background:var(--brand-blue-light);border:1px solid #557;
  color:#d9e7f5;font-size:12px;text-align:center;line-height:34px}

/* sidebar */
.side-head{left:450px;width:180px;height:25px;background:linear-gradient(#e6e6e6,#a9a9a9);font-size:13px;color:#333;padding:5px 8px;border-radius:2px}
.news{left:450px;top:258px;width:180px}
.news article{height:72px;border-bottom:1px solid #ccc;padding:5px 4px;position:relative}
.news time{font-size:7px;display:block}
.news q{display:block;margin:10px 0 0 15px;font-size:7.5px;line-height:9px;color:#333;quotes:none}
.news .read{position:absolute;right:12px;bottom:5px;font-size:7.5px;font-weight:700}
.partner{left:462px;top:491px;width:155px;height:234px;background:linear-gradient(#f6f9fd,#d4e5f5 30%,#3f7cc4 75%,#9fc6ea)}
.partner span{position:absolute;left:10px;top:14px;font-size:17px;color:#2a6db8}
.testimonial{left:452px;width:178px;height:62px;display:flex;gap:8px}
.testimonial .photo{width:34px;height:34px;background:linear-gradient(#cfcfcf,#8a8a8a);flex:none}
.testimonial blockquote{font-size:7.5px;line-height:9px}
.testimonial cite{display:block;text-align:right;font-style:normal;margin:6px 10px 0 0}

.footer{left:0;top:933px;width:633px;height:98px;background:var(--footer);color:var(--footer-text);text-align:center}
.footer nav{margin-top:12px;font-size:9.5px}
.footer nav span{margin:0 6px}
.follow{display:flex;justify-content:center;align-items:center;gap:6px;margin-top:16px;font-size:9px}
.follow i{width:28px;height:28px;border-radius:6px;background:#4aa3d9}
.follow i:nth-child(3){background:#3b5c9a}
.follow i:nth-child(4){background:#2a7ab0}
.copy{font-size:9px;margin-top:10px}
</style>
</head>
<body>
<header>
  <div class="abs logo-tab"><span class="mark"></span><span class="name">TradeoCup™</span></div>
  <div class="abs account-links"><a href="#">Register</a><a href="#">Login</a></div>
  <div class="abs countdown-label">Countdown</div>
  <div class="abs countdown">
    <div class="digits"><span>13<small>d</small></span><span>5<small>h</small></span><span>25<small>m</small></span><span>59<small>s</small></span></div>
    <div class="check">▸ Check Schedule</div>
  </div>
  <div class="abs lang"><div class="select">English</div><div class="flag"></div></div>
  <div class="abs participants"><div class="label">Round Participans</div><div class="count">840</div></div>
  <nav class="abs main-nav">
    <a href="#">About</a><a href="#">News</a><a href="#">Standings</a><a href="#">Schedule</a><a href="#">FAQ</a><a href="#">Brokker</a><a href="#">Download</a>
  </nav>
</header>

<main class="abs shell">
  <section class="abs hero" role="img" aria-label="Photo of business people running through a finish line on a stadium track">
    <p>TradeoCup™ is an international trading competition to see who can make the most profit in two weeks with all players getting an equal starting sum. Participation is free no strings attached and the prize money is real, with a total prize pool of $50,000</p>
    <a class="more">Find out more</a>
    <div class="join">JOIN NOW</div>
    <div class="dots"><i></i><i></i><i></i></div>
  </section>
  <aside class="abs prize">Prize Found<br>block</aside>

  <section class="abs panel tournaments">
    <div class="tabs"><span class="active">Current Tournaments</span><span>Ended Tournaments</span><span>Players Rating</span></div>
    <div class="tab-body">
      <p>Duis aute irure in reprehenderit in voluptate velit esse cillum dolore eu fugiat nulla pariatur. Excepteur sint occaecat cupidatat non proident, sunt in culpa qui officia deserunt mollit anim id est laborum.</p>
      <p><b>Lorem ipsum dolor sit amet,</b> consectetur adipiscing elit. Sed do eiusmod tempor incididunt ut labore et dolore magna aliqua. Ut enim ad minim veniam, quis nostrud exercitation ullamco laboris nisi ut aliquip ex ea commodo consequat. Duis aute irure dolor in reprehenderit in voluptate velit esse cillum dolore eu fugiat nulla pariatur. Excepteur sint occaecat cupidatat non proident, sunt in culpa qui officia deserunt mollit anim id est laborum.</p>
      <p>Duis aute irure in reprehenderit in voluptate velit esse cillum dolore eu fugiat nulla pariatur. Excepteur sint occaecat cupidatat non proident, sunt in culpa qui officia deserunt mollit anim id est laborum.</p>
      <p><b>Lorem ipsum dolor sit amet,</b> consectetur adipiscing elit. Sed do eiusmod tempor incididunt ut labore et dolore magna aliqua. Ut enim ad minim veniam, quis nostrud exercitation ullamco laboris nisi ut aliquip ex ea commodo consequat. Duis aute irure dolor in reprehenderit in voluptate velit esse cillum dolore eu fugiat nulla pariatur. Excepteur sint occaecat cupidatat non proident, sunt in culpa qui officia deserunt mollit anim id est laborum.</p>
      <p>Duis aute irure in reprehenderit in voluptate velit esse cillum dolore eu fugiat nulla pariatur. Excepteur sint occaecat cupidatat non proident, sunt in culpa qui officia deserunt mollit anim id est laborum.</p>
      <p><b>Lorem ipsum dolor sit amet,</b> consectetur adipiscing elit. Sed do eiusmod tempor incididunt ut labore et dolore magna aliqua. Ut enim ad minim veniam, quis nostrud exercitation ullamco laboris nisi ut aliquip ex ea commodo consequat. Duis aute irure dolor in reprehenderit in voluptate velit esse cillum dolore eu fugiat nulla pariatur. Excepteur sint occaecat cupidatat non proident, sunt in culpa qui officia deserunt mollit anim id est laborum.</p>
    </div>
  </section>

  <section class="abs panel map-panel">
    <div class="map" role="img" aria-label="World map with participating regions highlighted in blue"><span>REST OF THE WORLD</span></div>
  </section>
  <section class="abs panel banner-panel"><div class="banner">468X60</div></section>

  <h2 class="abs side-head" style="top:230px">Latest News</h2>
  <div class="abs news">
    <article><time>20/06/2011 | Monday</time><q>"lorem ipsum dolor sit amet, consectetur adipiscing elit. In convalis gravida neque..."</q><span class="read">read more</span></article>
    <article><time>20/06/2011 | Monday</time><q>"lorem ipsum dolor sit amet, consectetur adipiscing elit. In convalis gravida neque..."</q><span class="read">read more</span></article>
    <article><time>20/07/2011 | Monday</time><q>"lorem ipsum dolor sit amet, consectetur adipiscing elit. In convalis gravida neque..."</q><span class="read">read more</span></article>
  </div>
  <div class="abs partner" role="img" aria-label="Harbor Markets partner banner with a globe and city skyline"><span>Harbor Markets</span></div>
  <h2 class="abs side-head" style="top:738px">Testimonials</h2>
  <div class="abs testimonial" style="top:782px">
    <div class="photo" role="img" aria-label="Customer portrait"></div>
    <blockquote>"lorem ipsum dolor sit amet, con sectetuer adipiscing elit. In conva lis gravida neque. Ut enim ad min nim"<cite>Mark Ellis</cite></blockquote>
  </div>
  <div class="abs testimonial" style="top:850px">
    <div class="photo" role="img" aria-label="Customer portrait"></div>
    <blockquote>"lorem ipsum dolor sit amet, con sectetuer adipiscing elit. In conva lis gravida neque. Ut enim ad min nim"<cite>Paul Moran</cite></blockquote>
  </div>

  <footer class="abs footer">
    <nav>About<span>|</span>News<span>|</span>Standings<span>|</span>Schedule<span>|</span>FAQ<span>|</span>Brokker<span>|</span>Download<span>|</span>Live Chat<span>|</span>Terms &amp; Conditions<span>|</span>Contact Us</nav>
    <div class="follow"><span>FOLLOW US ON</span><i aria-label="Social network one"></i><i aria-label="Social network two"></i><i aria-label="Social network three"></i></div>
    <div class="copy">Copyright © 2011, tradeocup-example.com. All rights reserved.</div>
  </footer>
</main>
</body>
</html>
```